Communications Contractor Business Card Design

I would like a new business card for a new Communications company in Australia. Subcontracting and specialising in cabling, data, phone, antennas, pay tv ,modems, audio visual fibre optics etc. I am open to colour and design concepts but would like a modern clean look that stands out.

Industry/Entity Type

Tv

Contact Information for Business Card

quarzel communications pty ltd, Tomas Whitlock, PO BOX 527 Morrendale Flats QLD 4390 quarzel4me@mailbrook.net Australia. ph 0438271906. Director/Technician. services- Cabling,data,phone,antennas,audio visual,home theatre, fibre optics.

```html
<!DOCTYPE html>
<html lang="en">
<head>
<meta charset="utf-8">
<title>quarzel communications – business card</title>
<link href="https://fonts.googleapis.com/css2?family=Saira:wght@400;500&display=swap" rel="stylesheet">
<style>
  :root {
    --bg: #a9abae;
    --blue-deep: #0b63c0;
    --blue-mid: #1a86d8;
    --blue-light: #2fa6e6;
    --blue-text: #1c8ad6;
    --white: #ffffff;
    --grey-text: #6a6d70;
    --dark-text: #4a4c4e;
  }
  * { margin: 0; padding: 0; box-sizing: border-box; }
  html, body { width: 1200px; height: 900px; overflow: hidden; }
  body {
    background: var(--bg);
    font-family: "Saira", sans-serif;
    position: relative;
  }
  .card {
    position: absolute;
    left: 330px;
    width: 540px;
    height: 310px;
    overflow: hidden;
    box-shadow: 0 6px 18px rgba(0,0,0,0.25);
  }

  /* front */
  .card-front {
    top: 110px;
    background: linear-gradient(160deg, var(--blue-light) 0%, var(--blue-mid) 45%, var(--blue-deep) 100%);
    color: var(--white);
  }
  .front-band {
    position: absolute;
    left: 0; right: 0;
    top: 92px; height: 126px;
    background: rgba(255,255,255,0.08);
  }
  .front-watermark {
    position: absolute;
    left: -10px; top: 40px;
    font-size: 190px;
    font-weight: 400;
    line-height: 1;
    letter-spacing: -2px;
    color: rgba(255,255,255,0.09);
    white-space: nowrap;
  }
  .front-brand {
    position: absolute;
    right: 40px; top: 70px;
    text-align: right;
  }
  .front-name {
    font-size: 74px;
    font-weight: 500;
    line-height: 0.9;
    letter-spacing: -1px;
  }
  .front-sub {
    font-size: 17px;
    line-height: 1.2;
    margin-right: 6px;
  }
  .services {
    position: absolute;
    right: 40px; top: 198px;
    text-align: center;
    font-size: 13px;
    line-height: 1.25;
  }

  /* back */
  .card-back {
    top: 480px;
    background: var(--white);
    border-top: 4px solid var(--blue-mid);
  }
  .back-brand {
    position: absolute;
    left: 36px; top: 26px;
  }
  .back-name {
    font-size: 58px;
    font-weight: 500;
    line-height: 0.9;
    letter-spacing: -1px;
    color: var(--blue-text);
  }
  .back-sub {
    font-size: 14px;
    color: var(--grey-text);
    padding-left: 40px;
  }
  .contact {
    position: absolute;
    left: 36px; top: 140px;
    color: var(--dark-text);
  }
  .person {
    font-size: 25px;
    color: var(--blue-text);
    line-height: 1.1;
  }
  .role { font-size: 13px; margin-bottom: 10px; }
  .address { font-size: 13px; }
  .phone { font-size: 18px; line-height: 1.2; }
  .phone .label { color: var(--blue-text); font-size: 14px; }
  .back-band {
    position: absolute;
    left: 0; right: 0; bottom: 0;
    height: 34px;
    background: linear-gradient(90deg, var(--blue-deep), var(--blue-light));
  }
</style>
</head>
<body>
  <section class="card card-front">
    <div class="front-band"></div>
    <div class="front-watermark" aria-hidden="true">quarzel</div>
    <div class="front-brand">
      <div class="front-name">quarzel</div>
      <div class="front-sub">communications pty ltd</div>
    </div>
    <div class="services">
      services:<br>
      cabling / data / phone / antennas / audio visual<br>
      home theatre / fibre optics
    </div>
  </section>

  <section class="card card-back">
    <div class="back-brand">
      <div class="back-name">quarzel</div>
      <div class="back-sub">communications pty ltd</div>
    </div>
    <div class="contact">
      <div class="person">Tomas Whitlock</div>
      <div class="role">Director/Technician</div>
      <div class="address">PO BOX 527 Morrendale Flats QLD 4390 Australia</div>
      <div class="phone"><span class="label">ph:</span> 0438271906</div>
    </div>
    <div class="back-band"></div>
  </section>
</body>
</html>
```